Birchmont Entreprise Campus Media Package

We are looking for a designer to unify our company's image throughout its stationery and marketing deliverables. We will be focusing on:
*Business Cards (3.5 x 2)
*Letter Head (Letter Size)
*PowerPoint Presentation Template,
*One Pager Flyer (Letter Size)
*Front of Elevator's bay: 4 photos of the elevator bays (two groups of 3 elevators) to which we are looking for designs for its doors and surrounding wall (vinyl prints)
*Font's suggestions
*Official color palette.
*Outdoor Street Signage: please use the following dimensions:
Sign #1 (Delford Side): 48(W)x72"(H) (3 sided)
Sign #2: 24"(W)x48"(H) (3 sided)
Sign #3 (Top of Hill): 30(W)x54(H) (2 sides)
*Carport Sign:
See photos attached. The white letters will be removed, and a new sign will take place. Preferably, Cut-Out fonts, but we can consider an alternative approach for cost effective solution.
Find attached the approved logos.
______________________________________
We are a real estate holding company focused on the commercial office space in the Ohio, US, market.
You can check our site at www.birchmontcampus-example.com
As inspiration guidelines, we would like to see designs that are modern, minimalistic, dynamic and energetic.
Target Market(s)
General Population, Business Owners, Non-Profit Organizations, Government
Industry/Entity Type
Real Estate - Commercial Office Space - Flex Space

```html
<!DOCTYPE html>
<html lang="en">
<head>
<meta charset="utf-8">
<title>Birchmont Entreprise Campus – Flyer</title>
<link rel="stylesheet" href="https://fonts.googleapis.com/css2?family=Montserrat:wght@800&family=Poppins:wght@300;400;500;600&display=swap">
<style>
  :root {
    --paper: #e2e3e7;
    --ink: #2b2b2d;
    --brand-blue: #0a4aa6;
    --sky-top: #0d83c6;
    --sky-bottom: #1a9ad9;
    --accent-cyan: #86e6f2;
    --white: #ffffff;
    --footer-bar: #3b3b3e;
  }
  * { box-sizing: border-box; margin: 0; padding: 0; }
  html, body { width: 953px; height: 1200px; overflow: hidden; background: var(--paper); }
  .flyer {
    position: relative; width: 953px; height: 1200px; overflow: hidden;
    background: var(--paper); font-family: "Poppins", sans-serif; color: var(--ink);
  }

  /* Brand block */
  .brand {
    position: absolute; left: 0; top: 0; width: 392px; height: 349px;
    display: flex; flex-direction: column; align-items: center; justify-content: center;
    gap: 6px; color: var(--ink); font-weight: 500;
  }
  .brand-mark { width: 96px; height: 96px; border-radius: 50%; border: 2px solid var(--ink); margin-bottom: 14px; }
  .brand-name { font-size: 40px; letter-spacing: 1px; line-height: 1; }
  .brand-sub { font-size: 20px; line-height: 1.2; }

  /* Contact band */
  .contact {
    position: absolute; left: 0; top: 349px; width: 392px; height: 161px;
    background: var(--brand-blue); color: var(--white);
    list-style: none; padding: 30px 0 0 38px;
  }
  .contact li { display: flex; align-items: center; gap: 14px; height: 33.5px; font-size: 19px; letter-spacing: -0.5px; }
  .contact svg { width: 20px; height: 20px; fill: var(--white); flex: none; }

  /* Why choose us */
  .why { position: absolute; left: 33px; top: 538px; width: 350px; color: var(--brand-blue); }
  .why h2 { font-family: "Montserrat", sans-serif; font-weight: 800; font-size: 29px; letter-spacing: -1.5px; margin-bottom: 14px; }
  .why ul { list-style: none; }
  .why li { font-size: 17px; letter-spacing: -0.6px; height: 36px; display: flex; align-items: center; gap: 8px; }
  .why li::before { content: ""; width: 6px; height: 6px; border-right: 1.5px solid currentColor; border-top: 1.5px solid currentColor; transform: rotate(45deg); margin-right: 2px; }

  /* Services panel */
  .services {
    position: absolute; left: 392px; top: 0; width: 561px; height: 779px;
    background: linear-gradient(160deg, var(--sky-top), var(--sky-bottom));
    border-bottom-left-radius: 14px; color: var(--white);
  }
  .services-notch { position: absolute; left: 0; top: 69px; width: 22px; height: 64px; }
  .services-intro {
    position: absolute; left: 47px; top: 54px; width: 470px;
    font-size: 26px; line-height: 31px; letter-spacing: -1.2px; font-weight: 400;
  }
  .services-title {
    position: absolute; left: 42px; top: 178px; height: 415px;
    writing-mode: vertical-rl; transform: rotate(180deg);
    font-family: "Montserrat", sans-serif; font-weight: 800; font-size: 62px;
    letter-spacing: 1px; line-height: 1; text-align: center;
  }
  .service { position: absolute; left: 134px; width: 380px; }
  .service h3 { font-weight: 600; font-size: 22px; letter-spacing: -1px; color: var(--accent-cyan); margin-bottom: 8px; line-height: 1.2; }
  .service p { font-weight: 300; font-size: 13.5px; line-height: 15.5px; text-align: justify; }
  .service-1 { top: 176px; } .service-2 { top: 326px; } .service-3 { top: 475px; }

  /* Photography */
  .photo-towers {
    position: absolute; left: 345px; top: 616px; width: 608px; height: 584px;
    background: linear-gradient(180deg, rgba(226,234,242,0) 0%, #3f86c4 18%, #2a6fae 55%, #1f5d94 80%, #3f6e45 100%);
  }
  .photo-skyline {
    position: absolute; left: 0; top: 780px; width: 345px; height: 420px;
    background: linear-gradient(180deg, rgba(226,227,231,0) 0%, #d3d6dc 40%, #a9b0b8 75%, #4c6c3c 100%);
  }

  /* Footer */
  .web {
    position: absolute; left: 289px; top: 1155px; width: 360px; height: 45px;
    background: var(--footer-bar); border-radius: 10px 10px 0 0;
    color: #f1f1f1; font-weight: 300; font-size: 16px; letter-spacing: 0.3px;
    display: flex; align-items: center; justify-content: center;
  }
</style>
</head>
<body>
<main class="flyer">

  <header class="brand">
    <span class="brand-mark"></span>
    <span class="brand-name">BIRCHMONT</span>
    <span class="brand-sub">Entreprise Campus</span>
  </header>

  <ul class="contact">
    <li>
      <svg viewBox="0 0 24 24"><path d="M6.6 10.8a15.1 15.1 0 0 0 6.6 6.6l2.2-2.2a1 1 0 0 1 1-.25 11.4 11.4 0 0 0 3.6.57 1 1 0 0 1 1 1V20a1 1 0 0 1-1 1A17 17 0 0 1 3 4a1 1 0 0 1 1-1h3.5a1 1 0 0 1 1 1c0 1.25.2 2.45.57 3.57a1 1 0 0 1-.25 1z"/></svg>
      555-014-2207
    </li>
    <li>
      <svg viewBox="0 0 24 24"><path d="M12 2a7 7 0 0 0-7 7c0 5.2 7 13 7 13s7-7.8 7-13a7 7 0 0 0-7-7zm0 9.5A2.5 2.5 0 1 1 12 6.5a2.5 2.5 0 0 1 0 5z"/></svg>
      Lorem Ipsum, 123,
    </li>
    <li>
      <svg viewBox="0 0 24 24"><path d="M2 5h20v2l-10 6L2 7z"/><path d="M2 9.3l10 6 10-6V19H2z"/></svg>
      office@birchmont-example.com
    </li>
  </ul>

  <section class="why">
    <h2>WHY CHOOSE US?</h2>
    <ul>
      <li>Lorem Ipsum is simply dummy</li>
      <li>Lorem Ipsum is simply dummy</li>
      <li>Lorem Ipsum is simply dummy</li>
      <li>Lorem Ipsum is simply dummy</li>
      <li>Lorem Ipsum is simply dummy</li>
    </ul>
  </section>

  <div class="photo-skyline" role="img" aria-label="Photo of a distant office tower among clouds and green trees"></div>

  <section class="services">
    <svg class="services-notch" viewBox="0 0 22 64" preserveAspectRatio="none"><polygon points="0,0 22,32 0,64" fill="#e2e3e7"/></svg>
    <p class="services-intro">Lorem Ipsum is simply dummy text of the printing and typesetting industry.</p>
    <h2 class="services-title">SERVICES</h2>
    <article class="service service-1">
      <h3>Dummy Text</h3>
      <p>Lorem Ipsum is simply dummy text of the printing and typesetting industry. Lorem Ipsum has been the industry's standard dummy text ever since the 1500s</p>
    </article>
    <article class="service service-2">
      <h3>Dummy Text</h3>
      <p>Lorem Ipsum is simply dummy text of the printing and typesetting industry. Lorem Ipsum has been the industry's standard dummy text ever since the 1500s</p>
    </article>
    <article class="service service-3">
      <h3>Dummy Text</h3>
      <p>Lorem Ipsum is simply dummy text of the printing and typesetting industry. Lorem Ipsum has been the industry's standard dummy text ever since the 1500s</p>
    </article>
  </section>

  <div class="photo-towers" role="img" aria-label="Photo of blue glass office towers against a sky with clouds, trees at their base"></div>

  <footer class="web">www.birchmontcampus-example.com</footer>

</main>
</body>
</html>
```